E-Commerce Custom Design Magento Standard Requirements For Marketing Agency

I need to revamp theme for a website www.plinthwavestudio.com and want to change name to www.plinthwavehomes.com I have logo attached. I need a custom e commerce website built that pops and grabs attention. My logo is silver and looks great on black background. Please just use all same content from existing website www.plinthwavestudio.com and use existing products that you see there.

Target Market(s)

REAL ESTATE AGENTS

Industry/Entity Type

Digital Marketing

Coding

Coded - Design and coding required

Number of Pages Required

5+ page

Colors

Designer to choose colors to be used in the design.

Requirements
Must have
• Please revamp entire website www.plinthwavestudio.com and use new logo attached. Domain name will be www.plinthwavehomes.com and will offer marketing services for real estate agents around the country and world. Specializing in digital marketing services such as Vellumly Ads, Pictoraze Ads, Quip Loop Ads, Zarbit Promoworks, Etc.
Nice to have
Should not have

```html
<!DOCTYPE html>
<html lang="en">
<head>
<meta charset="utf-8">
<title>Plinthwave Homes — Advanced Marketing Services</title>
<link href="https://fonts.googleapis.com/css2?family=Montserrat:wght@400;500;600;700&display=swap" rel="stylesheet">
<style>
:root{
  --ink:#1c1c1c;
  --text:#333;
  --muted:#8a8a8a;
  --line:#d9d9d9;
  --white:#fff;
  --gold:#f0b21c;
  --teal:#1db5a2;
  --band:#efeef2;
  --footer:#1e1e1e;
  --footer-text:#bdbdbd;
}
*{margin:0;padding:0;box-sizing:border-box}
html,body{width:1200px;height:4215px;overflow:hidden;background:var(--white)}
body{font-family:'Montserrat',sans-serif;color:var(--text);position:relative}
.abs{position:absolute}
section,header,footer{position:absolute;left:0;width:1200px}

/* header */
.top-rule{top:0;height:6px;background:#6d6d6d;z-index:3}
.site-header{top:0;height:112px;background:var(--white);z-index:2}
.brand-plate{position:absolute;left:126px;top:20px;width:152px;height:152px;border-radius:50%;background:var(--white);display:flex;align-items:center;justify-content:center;text-align:center;z-index:4}
.brand-name{font-weight:600;font-size:15px;letter-spacing:2px;color:var(--ink);line-height:1.35;text-transform:uppercase}
.main-nav{position:absolute;top:52px;left:450px;display:flex;gap:0}
.main-nav a{position:absolute;font-size:14px;font-weight:500;color:var(--ink);text-decoration:none;letter-spacing:.5px;white-space:nowrap}
.nav-icon{position:absolute;top:48px}
.cart-count{position:absolute;left:1024px;top:64px;width:16px;height:16px;border-radius:50%;background:var(--ink);color:var(--white);font-size:9px;display:flex;align-items:center;justify-content:center}

/* hero */
.hero{top:112px;height:540px;background:linear-gradient(100deg,#2a3038 0%,#39424c 40%,#5a636b 65%,#2b3038 100%)}
.hero-kicker{left:174px;top:158px;font-size:16px;font-weight:500;color:var(--white);letter-spacing:1px}
.hero-title{left:174px;top:225px;font-size:42px;font-weight:500;color:var(--white);line-height:62px}
.btn-outline{display:flex;align-items:center;justify-content:center;border:2px solid var(--white);color:var(--white);font-size:14px;font-weight:500;letter-spacing:.5px}
.hero .btn-outline{left:174px;top:394px;width:130px;height:50px}
.hero-arrow{top:258px}

/* promo */
.promos{top:652px;height:228px}
.promo{position:absolute;top:0;height:228px;width:600px}
.promo-left{left:0;background:linear-gradient(120deg,#4a5664,#2c3642 60%,#1e2630)}
.promo-right{left:600px;background:linear-gradient(110deg,#1f2529,#3a4247 45%,#59616a 100%)}
.promo-title{font-size:17px;font-weight:600;color:var(--white);letter-spacing:.5px}
.promo-sub{font-size:13px;color:#d6d6d6}
.shop-link{font-size:11px;font-weight:500;color:var(--white);text-decoration:underline;letter-spacing:.5px}

/* headings */
.section-title{width:1200px;left:0;text-align:center;font-size:32px;font-weight:600;color:var(--ink);letter-spacing:1px}

/* tabs */
.tabs{top:1052px;left:0;width:1200px;display:flex;justify-content:center;align-items:center;gap:30px;font-size:13px;font-weight:500}
.tabs .dot{width:10px;height:10px;border-radius:50%;background:#bcbcbc}
.tabs .off{color:#a8a8a8}
.tabs .on{color:var(--ink)}

/* products */
.product{position:absolute;width:232px}
.product-media{width:232px;height:162px;position:relative;overflow:hidden}
.ribbon{position:absolute;left:0;top:0;width:0;height:0;border-top:36px solid var(--teal);border-right:36px solid transparent}
.stars{color:var(--gold);font-size:14px;letter-spacing:1px;margin-top:33px;line-height:1}
.product-name{font-size:13px;font-weight:500;color:var(--ink);line-height:24px;margin-top:12px;text-transform:uppercase}
.price{margin-top:14px;font-size:14px;font-weight:500;color:var(--ink)}
.price s{color:#9a9a9a;font-weight:400;margin-right:14px}

/* sale */
.sale{top:1902px;height:397px;background:linear-gradient(100deg,#4a4f55 0%,#353a40 45%,#5b4a44 75%,#3a3230 100%)}
.sale-title{top:105px;width:1200px;text-align:center;color:var(--white);font-size:46px;font-weight:500;letter-spacing:1px}
.sale-sub{top:178px;width:1200px;text-align:center;color:var(--white);font-size:18px}
.sale .btn-outline{left:524px;top:239px;width:152px;height:44px}

/* deals & blogs */
.block-title{font-size:15px;font-weight:600;color:var(--ink);letter-spacing:.3px}
.pager{font-size:22px;color:var(--ink);line-height:1}
.timer{display:flex;gap:22px}
.timer .unit{text-align:center;width:62px}
.timer .circle{width:62px;height:62px;border-radius:50%;background:var(--ink);color:var(--white);font-size:18px;font-weight:600;display:flex;align-items:center;justify-content:center}
.timer .lbl{font-size:10px;color:#555;margin-top:12px;letter-spacing:.5px}
.blog{position:absolute;display:flex;gap:20px}
.blog-media{width:150px;height:176px}
.blog-date{font-size:18px;color:var(--ink);margin-top:2px}
.blog-title{font-size:13px;font-weight:600;color:var(--ink);line-height:20px;margin-top:12px}
.blog-excerpt{font-size:11px;color:#777;line-height:17px;margin-top:6px}
.read-more{font-size:11px;color:var(--ink);margin-top:10px;display:block}

/* newsletter */
.newsletter{top:3032px;height:304px;background:var(--band)}
.newsletter .section-title{top:62px}
.newsletter-note{top:129px;width:1200px;text-align:center;font-size:14px;color:#555}
.signup{left:270px;top:188px;width:660px;height:45px;display:flex}
.signup .field{flex:1;background:var(--white);font-size:12px;color:#666;display:flex;align-items:center;padding-left:28px}
.signup .submit{width:130px;background:var(--ink);color:var(--white);font-size:12px;font-weight:600;display:flex;align-items:center;justify-content:center;letter-spacing:.5px}

/* follow */
.gallery-item{position:absolute;top:3529px;width:232px;height:186px}

/* footer */
.site-footer{top:3827px;height:388px;background:var(--footer)}
.footer-brand{left:110px;top:82px;width:160px;text-align:center;color:var(--white);font-size:17px;font-weight:600;letter-spacing:2px;line-height:1.4}
.footer-col{position:absolute;top:72px}
.footer-col h4{font-size:15px;font-weight:600;color:var(--white);letter-spacing:.5px;margin-bottom:20px}
.footer-col li{list-style:none;font-size:12px;color:var(--footer-text);line-height:33px}
.contact-row{display:flex;gap:18px;font-size:12px;color:var(--footer-text);line-height:20px;margin-bottom:14px}
.contact-row svg{flex:none;margin-top:2px}
.social{top:282px;left:502px;display:flex;gap:8px}
.social span{width:42px;height:42px;border-radius:50%;border:2px solid #e6e6e6;display:block}
.copyright{top:350px;width:1200px;text-align:center;font-size:11px;color:var(--footer-text)}
</style>
</head>
<body>

<div class="abs top-rule" style="left:0;width:1200px"></div>

<header class="site-header">
  <nav class="main-nav" aria-label="Main">
    <a style="left:0">HOME</a>
    <a style="left:92px">PRODUCTS</a>
    <a style="left:217px">ABOUT</a>
    <a style="left:317px">CONTACT</a>
    <a style="left:430px">LOGIN</a>
  </nav>
  <svg class="nav-icon" style="left:962px" width="18" height="20" viewBox="0 0 18 20" aria-label="Account"><circle cx="9" cy="5.5" r="4.5" fill="#1c1c1c"/><path d="M1 19c0-5 3.5-7.5 8-7.5s8 2.5 8 7.5z" fill="#1c1c1c"/></svg>
  <svg class="nav-icon" style="left:1012px" width="22" height="20" viewBox="0 0 22 20" aria-label="Cart"><path d="M1 2h3l3 11h11l2-8H6" fill="none" stroke="#1c1c1c" stroke-width="2"/><circle cx="8" cy="17" r="1.6" fill="#1c1c1c"/><circle cx="17" cy="17" r="1.6" fill="#1c1c1c"/></svg>
  <span class="cart-count">0</span>
  <svg class="nav-icon" style="left:1066px" width="20" height="20" viewBox="0 0 20 20" aria-label="Search"><circle cx="8" cy="8" r="6.5" fill="none" stroke="#1c1c1c" stroke-width="2"/><path d="M13 13l6 6" stroke="#1c1c1c" stroke-width="2"/></svg>
</header>

<div class="brand-plate"><span class="brand-name">Plinthwave<br>Homes</span></div>

<section class="hero" role="img" aria-label="Photo of a realtor working on a laptop and tablet at a desk">
  <p class="abs hero-kicker">PLINTHWAVE HOMES</p>
  <h1 class="abs hero-title">Advanced Marketing Services<br>For The Plinthwave Realtor</h1>
  <span class="abs btn-outline">BUY NOW</span>
  <svg class="abs hero-arrow" style="left:50px" width="20" height="40" viewBox="0 0 20 40"><path d="M18 2L2 20l16 18" fill="none" stroke="#cfd3d7" stroke-width="1.5"/></svg>
  <svg class="abs hero-arrow" style="left:1128px" width="20" height="40" viewBox="0 0 20 40"><path d="M2 2l16 18L2 38" fill="none" stroke="#cfd3d7" stroke-width="1.5"/></svg>
</section>

<section class="promos">
  <div class="promo promo-left" role="img" aria-label="Photo of hands using a tablet with charts on a desk">
    <p class="abs promo-title" style="left:112px;top:138px">VELLUMLY REMARKETING CAMPAIGN</p>
    <span class="abs shop-link" style="left:264px;top:182px">SHOP NOW</span>
  </div>
  <div class="promo promo-right" role="img" aria-label="Photo of a smartphone showing a messaging app">
    <p class="abs promo-title" style="left:237px;top:60px">SAVINGS UPTO 75% OFF</p>
    <p class="abs promo-sub" style="left:237px;top:100px">Duis aute irure dolor reprehenderit</p>
    <span class="abs shop-link" style="left:237px;top:146px">SHOP NOW</span>
  </div>
</section>

<h2 class="abs section-title" style="top:973px">TOP INTERESTING</h2>
<div class="abs tabs">
  <span class="off">NEW PRODUCTS</span><span class="dot"></span><span class="on">ONSALE</span><span class="dot"></span><span class="on">FEATURED</span>
</div>

<article class="product" style="left:112px;top:1135px">
  <div class="product-media" role="img" aria-label="Illustration of a hand sketching social media icons" style="background:linear-gradient(135deg,#e8e4dc,#bfb8ab)"><span class="ribbon"></span></div>
  <div class="stars">★★★★★</div>
  <p class="product-name">Plinthwave<br>Social Growth Engine</p>
  <p class="price"><s>$349.00</s>$249.00</p>
</article>
<article class="product" style="left:360px;top:1135px">
  <div class="product-media" role="img" aria-label="Photo of an ads keyboard key" style="background:linear-gradient(135deg,#2c3e56,#5c6f88)"><span class="ribbon"></span></div>
  <div class="stars">★★★★★</div>
  <p class="product-name">Vellumly Ad for one<br>&nbsp;open house</p>
  <p class="price"><s>$349.00</s>$249.00</p>
</article>
<article class="product" style="left:607px;top:1135px">
  <div class="product-media" role="img" aria-label="Illustration of a megaphone with notification bubbles" style="background:linear-gradient(135deg,#e4eef0,#a9c6d0)"><span class="ribbon"></span></div>
  <div class="stars">★★★★★</div>
  <p class="product-name">All marketing services for<br>one open house</p>
  <p class="price"><s>$349.00</s>$249.00</p>
</article>
<article class="product" style="left:857px;top:1135px">
  <div class="product-media" role="img" aria-label="Photo of a voice mail button on a phone" style="background:linear-gradient(135deg,#3a3a3a,#7a1f1f)"><span class="ribbon"></span></div>
  <div class="stars">★★★★★</div>
  <p class="product-name">Voice broadcast marketing<br>for one open house</p>
  <p class="price"><s>$349.00</s>$249.00</p>
</article>

<article class="product" style="left:112px;top:1498px">
  <div class="product-media" role="img" aria-label="Photo of a photo-sharing app on a phone screen" style="background:linear-gradient(135deg,#6a3bb0,#d9457a 60%,#f0a040)"></div>
  <div class="stars">★★★★★</div>
  <p class="product-name">Pictoraze Ad for one<br>open house</p>
  <p class="price"><s>$349.00</s>$249.00</p>
</article>
<article class="product" style="left:360px;top:1498px">
  <div class="product-media" role="img" aria-label="Illustration of text message advertising puzzle pieces" style="background:linear-gradient(135deg,#dfe7ee,#8fb3cf)"><span class="ribbon"></span></div>
  <div class="stars">★★★★★</div>
  <p class="product-name">SMS marketing for one<br>open house</p>
  <p class="price"><s>$349.00</s>$249.00</p>
</article>
<article class="product" style="left:607px;top:1498px">
  <div class="product-media" role="img" aria-label="Illustration of an email marketing sign" style="background:linear-gradient(135deg,#1e3550,#4c6e92)"></div>
  <div class="stars">★★★★★</div>
  <p class="product-name">Email marketing for one<br>open house</p>
  <p class="price"><s>$349.00</s>$249.00</p>
</article>
<article class="product" style="left:857px;top:1498px">
  <div class="product-media" role="img" aria-label="Illustration of two social network icons side by side" style="background:linear-gradient(135deg,#eef0f4,#c7cfdb)"><span class="ribbon"></span></div>
  <div class="stars">★★★★★</div>
  <p class="product-name">Vellumly &amp; Pictoraze Ad combo<br>for one open house</p>
  <p class="price"><s>$349.00</s>$249.00</p>
</article>

<section class="sale" role="img" aria-label="Photo of hands typing on a laptop with floating reaction icons">
  <h2 class="abs sale-title">POPULAR SALE</h2>
  <p class="abs sale-sub">*Gift Cards excluded</p>
  <span class="abs btn-outline">SHOP NOW</span>
</section>

<h3 class="abs block-title" style="left:110px;top:2410px">DEALS OF THE WEEK</h3>
<span class="abs pager" style="left:385px;top:2405px">‹ ›</span>
<div class="abs" role="img" aria-label="Photo of a team planning around a table with devices" style="left:112px;top:2478px;width:304px;height:192px;background:linear-gradient(135deg,#3f6b8a,#c9a24a 50%,#6a4a3a)"></div>
<div class="abs stars" style="left:112px;top:2670px">★★★★★</div>
<p class="abs product-name" style="left:112px;top:2715px">PLINTHWAVE<br>SOCIAL GROWTH ENGINE</p>
<p class="abs price" style="left:112px;top:2788px"><s>$349.00</s>$249.00</p>
<p class="abs" style="left:112px;top:2830px;font-size:13px;font-weight:500;color:var(--ink)">HURRY UP ! OFFER ENDS IN</p>
<div class="abs timer" style="left:108px;top:2861px">
  <div class="unit"><div class="circle">178</div><p class="lbl">DAYS</p></div>
  <div class="unit"><div class="circle">34</div><p class="lbl">HRS</p></div>
  <div class="unit"><div class="circle">60</div><p class="lbl">MIN</p></div>
  <div class="unit"><div class="circle">12</div><p class="lbl">SECS</p></div>
</div>

<h3 class="abs block-title" style="left:450px;top:2410px">LATEST BLOGS</h3>
<span class="abs pager" style="left:1058px;top:2405px">‹ ›</span>

<article class="blog" style="left:450px;top:2478px">
  <div class="blog-media" role="img" aria-label="Photo of analytics dashboards on a monitor" style="background:linear-gradient(135deg,#27405a,#6b8aa8)"></div>
  <div><p class="blog-date">27 Aug</p><p class="blog-title">Lorem ipsum dolor<br>unde omnis iste</p><p class="blog-excerpt">Sed ut perspiciatis<br>unde omnis iste natus</p><span class="read-more">Read More</span></div>
</article>
<article class="blog" style="left:795px;top:2478px">
  <div class="blog-media" role="img" aria-label="Photo of a hand touching a digital network target" style="background:linear-gradient(135deg,#0f2a3c,#2f6c8c)"></div>
  <div><p class="blog-date">27 Aug</p><p class="blog-title">Lorem ipsum dolor<br>unde omnis iste</p><p class="blog-excerpt">Sed ut perspiciatis<br>unde omnis iste natus</p><span class="read-more">Read More</span></div>
</article>
<article class="blog" style="left:450px;top:2703px">
  <div class="blog-media" role="img" aria-label="Photo of hands typing on a laptop keyboard" style="background:linear-gradient(135deg,#b5533e,#e3c2b0)"></div>
  <div><p class="blog-date">27 Aug</p><p class="blog-title">Lorem ipsum dolor<br>unde omnis iste</p><p class="blog-excerpt">Sed ut perspiciatis<br>unde omnis iste natus</p><span class="read-more">Read More</span></div>
</article>
<article class="blog" style="left:795px;top:2703px">
  <div class="blog-media" role="img" aria-label="Photo of a laptop on a desk beside a notebook" style="background:linear-gradient(135deg,#c9ccd2,#6e7682)"></div>
  <div><p class="blog-date">27 Aug</p><p class="blog-title">Lorem ipsum dolor<br>unde omnis iste</p><p class="blog-excerpt">Sed ut perspiciatis<br>unde omnis iste natus</p><span class="read-more">Read More</span></div>
</article>

<section class="newsletter">
  <h2 class="abs section-title">JOIN OUR NEWSLETTER</h2>
  <p class="abs newsletter-note">Subscribe our newsletter for get notification about new updates, information discount, etc.</p>
  <div class="abs signup"><span class="field">Enter Email</span><span class="submit">SUBSCRIBE</span></div>
</section>

<h2 class="abs section-title" style="top:3434px">#FOLLOWS ON PICTORAZE</h2>
<div class="gallery-item" role="img" aria-label="Photo of a laptop with business charts" style="left:112px;background:linear-gradient(135deg,#d7dde4,#5d7f9f)"></div>
<div class="gallery-item" role="img" aria-label="Illustration of colourful network lines joining at a point" style="left:360px;background:linear-gradient(135deg,#eef0f2,#b9c3cc)"></div>
<div class="gallery-item" role="img" aria-label="Photo of marketing lettering on grey blocks" style="left:609px;background:linear-gradient(135deg,#9a9a9a,#3f3f3f 60%,#6e9a4a)"></div>
<div class="gallery-item" role="img" aria-label="Photo of a phone sending glowing envelopes" style="left:857px;background:linear-gradient(135deg,#2a2420,#a2693a 60%,#e8c89a)"></div>

<footer class="site-footer">
  <p class="abs footer-brand">PLINTHWAVE<br>HOMES</p>
  <div class="footer-col" style="left:351px"><h4>MY ACCOUNT</h4><ul><li>Order History</li><li>Contact Us</li><li>Site Map</li><li>Terms &amp; Condition</li></ul></div>
  <div class="footer-col" style="left:540px"><h4>INFORMATION</h4><ul><li>Privacy Policy</li><li>Delivery Information</li><li>Specials</li></ul></div>
  <div class="footer-col" style="left:736px"><h4>QUICK LINKS</h4><ul><li>Products</li><li>About</li><li>Contact</li><li>Login</li></ul></div>
  <div class="footer-col" style="left:905px"><h4>CONTACT US</h4>
    <div class="contact-row"><svg width="14" height="14" viewBox="0 0 14 14"><path d="M7 1L1 6.5h2V13h3V9h2v4h3V6.5h2z" fill="#e0e0e0"/></svg><span>123 Sed ut perspiciatis<br>unde omnis,</span></div>
    <div class="contact-row"><svg width="14" height="14" viewBox="0 0 14 14"><path d="M3 1l2.5 3-1.5 1.5c.8 1.8 2 3 3.5 3.5L9 7.5l3 2.5-1.5 2.5C6 12 2 8 1.5 3z" fill="#e0e0e0"/></svg><span>1 888 888 8888</span></div>
    <div class="contact-row"><svg width="14" height="14" viewBox="0 0 14 14"><rect x="1" y="3" width="12" height="9" fill="#e0e0e0"/><path d="M1 3l6 5 6-5" fill="none" stroke="#1e1e1e" stroke-width="1.2"/></svg><span>info@plinthwavehomes.com</span></div>
  </div>
  <div class="abs social" aria-label="Social profiles"><span></span><span></span><span></span><span></span></div>
  <p class="abs copyright">Copyrights 2018 Companyname.All Rights Reserved</p>
</footer>

</body>
</html>
```